Design new modern Business Cards

I'm looking for a new modern business card & Stationery design.
We are an Architectural Lighting business that imports products from Europe and Australasia.
see our website for further information: [url removed, login to view]
- Card is to be double sided.
- Design is to be based on 4 colours: White, Green, Grey and Black ( Can provide Colour Number)
- successful design is to be supplied in Indesign format for future updates.

```html
<!DOCTYPE html>
<html lang="en">
<head>
<meta charset="utf-8">
<title>Lumaverde business card</title>
<link rel="stylesheet" href="https://fonts.googleapis.com/css2?family=Montserrat:wght@300;400;500&display=swap">
<style>
  :root {
    --page: #e9e7e3;
    --white: #ffffff;
    --green: #8cbd2c;
    --green-dark: #76a51f;
    --green-light: #a6d04a;
    --grey: #6d6f71;
    --grey-soft: #c9cbc7;
    --black: #1e1f1d;
  }
  * { margin: 0; padding: 0; box-sizing: border-box; }
  html, body { width: 1200px; height: 817px; overflow: hidden; }
  body {
    background: var(--page);
    font-family: "Montserrat", sans-serif;
    display: flex;
    flex-direction: column;
    align-items: center;
    justify-content: center;
    gap: 40px;
  }
  .card {
    position: relative;
    width: 620px;
    height: 354px;
    border-radius: 22px;
    overflow: hidden;
    background: var(--white);
    box-shadow: 0 6px 18px rgba(0,0,0,.12);
  }
  .card__shapes { position: absolute; inset: 0; width: 100%; height: 100%; }

  /* front */
  .brand {
    position: absolute; left: 42px; top: 46px;
    font-weight: 400; font-size: 44px; letter-spacing: 1px;
    color: var(--grey); line-height: 1;
  }
  .tagline {
    position: absolute; left: 46px; top: 98px;
    font-size: 9px; font-weight: 500; letter-spacing: 2.4px;
    color: var(--black); text-transform: uppercase;
  }
  .social { position: absolute; left: 60px; top: 124px; display: flex; gap: 12px; }
  .social__dot { width: 22px; height: 22px; border: 1.5px solid var(--grey); border-radius: 50%; }
  .product-shot { position: absolute; left: 380px; top: 150px; width: 210px; height: 150px; }

  /* back */
  .brand--faint {
    left: 34px; top: 40px; font-size: 46px;
    color: var(--green-light);
  }
  .back-info { position: absolute; right: 30px; top: 70px; text-align: right; }
  .back-info__name {
    font-size: 24px; font-weight: 400; letter-spacing: 1px;
    color: var(--black); margin-bottom: 26px;
  }
  .contact { list-style: none; }
  .contact__item {
    display: flex; align-items: center; justify-content: flex-end; gap: 12px;
    font-size: 15px; font-weight: 400; color: var(--black);
    height: 38px;
  }
  .contact__icon {
    width: 22px; height: 22px; border-radius: 50%;
    border: 1.5px solid var(--green);
    display: flex; align-items: center; justify-content: center;
  }
  .contact__icon svg { width: 12px; height: 12px; fill: none; stroke: var(--green-dark); stroke-width: 2; }
</style>
</head>
<body>

<section class="card card--front">
  <svg class="card__shapes" viewBox="0 0 620 354" aria-hidden="true">
    <polygon points="0,240 330,175 620,60 620,354 0,354" fill="var(--green)"/>
    <polygon points="0,240 330,175 250,354 0,354" fill="var(--green-dark)"/>
    <polygon points="330,175 620,60 620,210" fill="var(--green-light)"/>
    <polygon points="250,354 330,175 420,354" fill="var(--green-light)" opacity=".55"/>
  </svg>
  <div class="brand">LUMAVERDE</div>
  <div class="tagline">Architectural + Bespoke Lighting</div>
  <div class="social"><span class="social__dot"></span><span class="social__dot"></span></div>
  <svg class="product-shot" viewBox="0 0 210 150" role="img" aria-label="Photo of a black architectural track spotlight">
    <defs>
      <linearGradient id="lampTone" x1="0" y1="0" x2="1" y2="1">
        <stop offset="0" stop-color="#4a4d48"/>
        <stop offset="1" stop-color="#1e1f1d"/>
      </linearGradient>
    </defs>
    <rect x="0" y="0" width="210" height="150" rx="40" fill="url(#lampTone)"/>
  </svg>
</section>

<section class="card card--back">
  <svg class="card__shapes" viewBox="0 0 620 354" aria-hidden="true">
    <rect width="620" height="354" fill="var(--green)"/>
    <polygon points="0,0 300,0 240,190 0,130" fill="var(--green-light)" opacity=".5"/>
    <polygon points="0,354 240,190 330,354" fill="var(--green-dark)"/>
    <polygon points="300,0 620,0 620,354 330,354 240,190" fill="var(--white)"/>
    <polygon points="300,0 360,0 240,190" fill="var(--grey-soft)" opacity=".5"/>
  </svg>
  <div class="brand brand--faint">LUMAVERDE</div>
  <div class="back-info">
    <div class="back-info__name">LUMAVERDE</div>
    <ul class="contact">
      <li class="contact__item">0400 218 734
        <span class="contact__icon"><svg viewBox="0 0 12 12"><path d="M3 1 L5 3 L4 5 Q5 7 7 8 L9 7 L11 9 L9 11 Q4 10 1 3 Z"/></svg></span></li>
      <li class="contact__item">info@lumaverde.com.au
        <span class="contact__icon"><svg viewBox="0 0 12 12"><rect x="1" y="3" width="10" height="7"/><path d="M1 3 L6 7 L11 3"/></svg></span></li>
      <li class="contact__item">Greenvale Ridge 3150 Australia.
        <span class="contact__icon"><svg viewBox="0 0 12 12"><path d="M6 11 Q2 6 2 4.5 A4 4 0 0 1 10 4.5 Q10 6 6 11 Z"/><circle cx="6" cy="4.5" r="1.2"/></svg></span></li>
      <li class="contact__item">lumaverde.com.au
        <span class="contact__icon"><svg viewBox="0 0 12 12"><circle cx="6" cy="6" r="5"/><path d="M1 6 H11 M6 1 Q3 6 6 11 M6 1 Q9 6 6 11"/></svg></span></li>
    </ul>
  </div>
</section>

</body>
</html>
```